Asia based real estate financing firm needs and AWESOME design for a biz card -Harbor Lending Circle

Looking for a stylish, & corporate-looking business card for a real estate financing brokerage firm in Asia, offering global mortgage loans. I uploaded our current logos. We would like to add a splash of color (perhaps the house icon) or any other suggestions are open. For the winning designer, we have a lot of work! Thanks and best of luck!

Target Market(s)

Real estate investors globally. We want to look more like a BANK and NOT a real estate company. Please don't play up on a "house" design.

Industry/Entity Type

Banking

Contact Information for Business Card

Harbor Lending Circle
Peter Wilks
Co-Founder | Partner

14 Cassia Lane, Suite 310
Singapore 047219
www.hlc-example.asia
peterwilks@hlc-example.asia
+65 555-0142
WeChat: peterwilks

Colors

Designer to choose colors to be used in the design.

Requirements
Must have
• Must have the standard business requirements for a card; name, address, email, etc
• Can be horizontal or vertical.
Nice to have
• It would be great to see some sort of variation to the logo with a pop of color. Red is good as we're in Asia, however, other options work as well.
• Our tag line is - Borderless mortgages. It doesn't have to be on the card but might be nice.
• I'd like to start seeing our tagline within the cards as well. - Borderless mortgages.
• Also, please add our location. The location for this card is Singapore so perhaps it can be highlighted or emphasised in some way.
• Singapore | Hong Kong | Shanghai | Manila
• As we will soon open an office in Shanghai, having an option for both languages would be great.
Should not have
• I'm exceited and open to your creativity ... knock it out of the park!

```html
<!DOCTYPE html>
<html lang="en">
<head>
<meta charset="utf-8">
<title>Harbor Lending Circle – Business Card</title>
<link rel="stylesheet" href="https://fonts.googleapis.com/css2?family=Cinzel:wght@400&family=Noto+Serif:ital,wght@0,700;1,400;1,700&family=Open+Sans:wght@400&display=swap">
<style>
  :root {
    --bg: #ece9e4;
    --card-white: #f4f4f4;
    --card-white-edge: #dcdcdc;
    --brand-red: #d41f24;
    --card-red: #c9242d;
    --card-red-dark: #a81a21;
    --social-blue: #1e8fd6;
    --text-grey: #6f6f6f;
    --white: #ffffff;
  }
  * { margin: 0; padding: 0; box-sizing: border-box; }
  html, body { width: 1200px; height: 1023px; overflow: hidden; }
  body { background: var(--bg); position: relative; font-family: "Noto Serif", serif; }

  .card {
    position: absolute;
    width: 640px;
    height: 366px;
    border-radius: 18px;
    box-shadow: 0 6px 18px rgba(0,0,0,0.18);
  }

  /* Front */
  .card-front {
    left: 70px; top: 80px;
    background: linear-gradient(160deg, var(--card-white) 0%, #e6e6e6 100%);
    border: 1px solid var(--card-white-edge);
    display: flex;
    flex-direction: column;
    align-items: center;
    justify-content: space-between;
    padding: 110px 40px 30px;
  }
  .front-brand {
    font-family: "Cinzel", serif; font-weight: 400;
    color: var(--brand-red);
    font-size: 44px; letter-spacing: 1px; line-height: 1.1;
    white-space: nowrap;
    text-align: center;
  }
  .social-row {
    align-self: stretch;
    display: flex; justify-content: space-between;
    font-family: "Open Sans", sans-serif; font-size: 13px; color: var(--text-grey);
  }
  .social-item { display: flex; align-items: center; gap: 7px; }
  .social-dot { width: 11px; height: 11px; border-radius: 50%; background: var(--social-blue); }

  /* Back */
  .card-back {
    left: 500px; top: 580px;
    background: linear-gradient(150deg, var(--card-red) 0%, #d02a33 50%, var(--card-red-dark) 100%);
    color: var(--white);
    overflow: hidden;
  }
  .back-brand {
    position: absolute; left: 36px; top: 96px; width: 230px;
    font-family: "Cinzel", serif; font-weight: 400;
    font-size: 38px; line-height: 1.2; color: var(--white);
  }
  .back-divider {
    position: absolute; left: 290px; top: 40px; bottom: 40px;
    width: 1px; background: rgba(255,255,255,0.75);
  }
  .back-contact { position: absolute; left: 318px; top: 40px; right: 30px; }
  .person-name { font-weight: 700; font-style: italic; font-size: 22px; line-height: 1.2; }
  .person-title { font-weight: 700; font-style: italic; font-size: 13px; margin-top: 2px; }
  .contact-rule { height: 1px; background: rgba(255,255,255,0.75); margin: 14px 0 16px; }
  .contact-list { list-style: none; font-style: italic; font-size: 14px; line-height: 1.55; }
  .contact-list li { display: flex; align-items: flex-start; gap: 10px; }
  .contact-list svg { flex: none; width: 14px; height: 14px; margin-top: 4px; }
</style>
</head>
<body>

<section class="card card-front" aria-label="Business card front">
  <div class="front-brand">Harbor Lending Circle</div>
  <div class="social-row">
    <span class="social-item"><span class="social-dot"></span>harborlendingcircle</span>
    <span class="social-item"><span class="social-dot"></span>harborlendingcircle</span>
    <span class="social-item"><span class="social-dot"></span>@harborlendingcircle</span>
  </div>
</section>

<section class="card card-back" aria-label="Business card back">
  <div class="back-brand">Harbor Lending Circle</div>
  <div class="back-divider"></div>
  <div class="back-contact">
    <div class="person-name">Peter Wilks</div>
    <div class="person-title">Co-Founder | Partner</div>
    <div class="contact-rule"></div>
    <ul class="contact-list">
      <li>
        <svg viewBox="0 0 14 14" aria-hidden="true"><path d="M7 1a4.5 4.5 0 0 0-4.5 4.5C2.5 9 7 13 7 13s4.5-4 4.5-7.5A4.5 4.5 0 0 0 7 1z" fill="#fff"/><circle cx="7" cy="5.5" r="1.6" fill="#c9242d"/></svg>
        <span>14 Cassia Lane, Suite 310<br>Singapore 047219</span>
      </li>
      <li>
        <svg viewBox="0 0 14 14" aria-hidden="true"><circle cx="7" cy="7" r="6" fill="none" stroke="#fff" stroke-width="1.2"/><path d="M5 4.2l1.2 1.6-.7.8c.4.9 1.1 1.6 2 2l.8-.7 1.6 1.2-.7 1.1C6.8 10 4 7.2 3.9 4.9z" fill="#fff"/></svg>
        <span>+65 555-0142</span>
      </li>
      <li>
        <svg viewBox="0 0 14 14" aria-hidden="true"><rect x="1.5" y="3" width="11" height="8" fill="none" stroke="#fff" stroke-width="1.2"/><path d="M1.5 3l5.5 4.5L12.5 3" fill="none" stroke="#fff" stroke-width="1.2"/></svg>
        <span>peterwilks@hlc-example.asia</span>
      </li>
      <li>
        <svg viewBox="0 0 14 14" aria-hidden="true"><circle cx="7" cy="7" r="5.6" fill="none" stroke="#fff" stroke-width="1.1"/><ellipse cx="7" cy="7" rx="2.4" ry="5.6" fill="none" stroke="#fff" stroke-width="1"/><path d="M1.4 7h11.2M2.3 4.2h9.4M2.3 9.8h9.4" stroke="#fff" stroke-width="0.9"/></svg>
        <span>www.hlc-example.asia</span>
      </li>
      <li>
        <svg viewBox="0 0 14 14" aria-hidden="true"><circle cx="7" cy="7" r="6" fill="#fff"/></svg>
        <span>peterwilks</span>
      </li>
    </ul>
  </div>
</section>

</body>
</html>
```